Dravetti Business Cards

We need a business card design for Dravetti Mining.

This is a B2B company that buys and sells large machinery tires within the coal mining industry. The design should the strong, crisp and masculine. I have uploaded the company logo and rough mock-up of what the back of the card should look like. the front of the card should have the same look/feel as the back. I need editable templates for both the front and the back of the card.

Color scheme should be grey/green/black

Contact information to include on the card:
Name: Owen Pellsworth
Title: Managing Director
Phone: 972-555-0143
Address: 3157 Brantley #5 Dallas, TX 75209
Email: Owen@Dravetti-example.com

I am also opening a contest for letterhead design. If you submit a business card design, please also submit a letterhead design with the same look/feel. The winner of the business card design will also will the letter head and be paid for both.

Target Market(s)

Procurement men/women in the coal mining industry

Industry/Entity Type

Coal Mining

```html
<!DOCTYPE html>
<html lang="en">
<head>
<meta charset="utf-8">
<title>Dravetti Mining – Business Card</title>
<link rel="stylesheet" href="https://fonts.googleapis.com/css2?family=Arimo:wght@400;700&display=swap">
<style>
  :root {
    --brand-green: #62a844;
    --text-grey: #58595b;
    --card-white: #ffffff;
    --page-bg: #ffffff;
    --card-edge: #111111;
  }
  * { margin: 0; padding: 0; box-sizing: border-box; }
  html, body {
    width: 1200px;
    height: 1000px;
    overflow: hidden;
    background: var(--page-bg);
    font-family: "Arimo", Helvetica, Arial, sans-serif;
  }
  .card {
    position: absolute;
    left: 76px;
    top: 200px;
    width: 1049px;
    height: 599px;
    background: var(--card-white);
    border: 2px solid var(--card-edge);
    box-shadow: 4px 6px 10px rgba(0, 0, 0, 0.22);
    overflow: hidden;
  }
  .side-panel {
    position: absolute;
    left: 672px;
    top: 0;
    right: 0;
    bottom: 0;
    background: var(--brand-green);
  }
  .divider-rule {
    position: absolute;
    top: 195px;
    height: 3px;
  }
  .divider-rule--left { left: 0; width: 672px; background: var(--brand-green); }
  .divider-rule--right { left: 672px; right: 0; background: var(--card-white); }

  .wordmark {
    position: absolute;
    left: 67px;
    top: 56px;
    display: flex;
    align-items: center;
    gap: 20px;
  }
  .wordmark__square {
    width: 58px;
    height: 58px;
    background: var(--brand-green);
  }
  .wordmark__name {
    font-weight: 700;
    font-size: 44px;
    letter-spacing: 1px;
    color: var(--text-grey);
    text-transform: uppercase;
    white-space: nowrap;
  }

  .person {
    position: absolute;
    left: 67px;
    top: 308px;
    color: var(--text-grey);
  }
  .person__name { font-size: 34px; font-weight: 400; letter-spacing: -0.3px; -webkit-text-stroke: 0.6px var(--text-grey); }
  .person__title { font-size: 26px; margin-top: 8px; }

  .contact {
    position: absolute;
    left: 67px;
    top: 480px;
    color: var(--text-grey);
    font-size: 26px;
    line-height: 36px;
  }

  .address {
    position: absolute;
    left: 718px;
    top: 482px;
    color: var(--card-white);
    font-size: 23px;
    line-height: 27px;
  }
</style>
</head>
<body>
  <div class="card">
    <div class="side-panel"></div>
    <div class="divider-rule divider-rule--left"></div>
    <div class="divider-rule divider-rule--right"></div>

    <div class="wordmark">
      <div class="wordmark__square"></div>
      <div class="wordmark__name">Dravetti Mining</div>
    </div>

    <div class="person">
      <p class="person__name">Owen Pellsworth</p>
      <p class="person__title">Managing Director</p>
    </div>

    <div class="contact">
      <p class="contact__phone">(972) 555-0143</p>
      <p class="contact__email">Owen@Dravetti-example.com</p>
    </div>

    <div class="address">
      <p>3157 Brantley Street, #5</p>
      <p>Dallas, TX 75209</p>
      <p>www.dravetti-example.com</p>
    </div>
  </div>
</body>
</html>
```